Diary toward Stillness - book cover

12/18 update: Please read the entire brief. I don’t love anything that has been provided up to today. Please use the graphics and colors I’ve attached!!!! Show me your creations.

I am looking for a book cover design. It is a mental health journal. Needs to be very warm, inviting, calming. I’m very interested in new creative ideas. It will be wire-o bound and also in hard copy front and back. Use the graphic and colors I already have attached to this file. It’s called “Diary Toward Stillness”. Self means soul or spirit or center. The idea of integration may be a fit here in some way. If some words need to be emphasized in the design, “Self” and “QMR” would be the most important. size 6"x9". The words on the front can be smaller and more inviting then they would normally be on a fiction paperback.

Update 12/16: I am not excited about any of the submissions so far. I’m looking forward to seeing more options.

Target Market(s)

Adults 30-60. Male and female. People who like to learn. People wanting to heal. Middle and upper income.

Industry/Entity Type

Mental health. Wellness

Other font styles liked:
• Whatever font is used in my logo. i don’t know the name. I also would be open to a different font if it was warm, inviting, and calm.

Colors
0094D4
00A9DD
6FCCEA
C7EBF8
E9F6FB

Requirements
Must have
• My logo colors. The words “Diary Toward Stillness” and “A 13-Week QMR Exploration”
Nice to have
• I’d like to see some creative ideas. More abstract than realistic.
Should not have
• No realist art or photos.

```html
<!DOCTYPE html>
<html lang="en">
<head>
<meta charset="utf-8">
<title>Diary Toward Stillness – Cover</title>
<link rel="stylesheet" href="https://fonts.googleapis.com/css2?family=Poiret+One&family=Josefin+Sans:wght@400&family=Great+Vibes&display=swap">
<style>
  :root {
    --page: #ffffff;
    --paper: #e9f6fb;
    --paper-tint: #c7ebf8;
    --wash: #6fccea;
    --panel-top: #0094d4;
    --panel-mid: #00a9dd;
    --panel-glow: #c7ebf8;
    --ink: #0094d4;
    --ink-deep: #0a6f9e;
  }
  * { margin: 0; padding: 0; box-sizing: border-box; }
  html, body {
    width: 1200px; height: 1200px; overflow: hidden;
    background: var(--page);
  }
  .cover {
    position: absolute;
    left: 216px; top: 50px;
    width: 768px; height: 1100px;
    background: var(--paper);
    overflow: hidden;
  }
  .wash {
    position: absolute; inset: 0;
    background:
      radial-gradient(ellipse 48% 22% at 72% 36%, rgba(111,204,234,0.55) 0%, rgba(111,204,234,0.25) 55%, rgba(111,204,234,0) 100%),
      radial-gradient(ellipse 60% 30% at 78% 64%, rgba(199,235,248,0.9) 0%, rgba(199,235,248,0) 100%),
      linear-gradient(180deg, var(--paper) 0%, var(--paper-tint) 100%);
  }
  .flock {
    position: absolute;
    left: 90px; top: 12px;
    width: 512px; height: 330px;
    background: radial-gradient(ellipse 50% 45% at 45% 50%, rgba(0,148,212,0.35) 0%, rgba(0,148,212,0) 100%);
  }
  .window-art {
    position: absolute;
    left: 294px; top: 371px;
    width: 181px; height: 394px;
    background: linear-gradient(180deg, var(--panel-top) 0%, var(--panel-top) 50%, var(--panel-mid) 78%, var(--panel-glow) 100%);
    box-shadow: 0 2px 6px rgba(0,80,120,0.25);
  }
  .title {
    position: absolute; inset: 0;
    font-weight: normal;
    color: var(--ink-deep);
  }
  .title__main {
    position: absolute;
    left: 120px; top: 838px;
    font-family: "Poiret One", sans-serif;
    font-size: 84px; line-height: 1;
    letter-spacing: 2px;
  }
  .title__sub {
    position: absolute;
    left: 150px; top: 928px;
    font-family: "Josefin Sans", sans-serif;
    font-weight: 400;
    font-size: 60px; line-height: 1;
  }
  .title__accent {
    position: absolute;
    left: 382px; top: 870px;
    font-family: "Great Vibes", cursive;
    font-size: 104px; line-height: 1;
    color: var(--ink);
    white-space: nowrap;
  }
  .subtitle {
    position: absolute;
    left: 150px; top: 1046px;
    font-family: "Poiret One", sans-serif;
    font-size: 30px; line-height: 1;
    letter-spacing: 1px;
    color: var(--ink-deep);
    white-space: nowrap;
  }
</style>
</head>
<body>
  <main class="cover">
    <div class="wash"></div>
    <div class="flock" role="img" aria-label="Flock of small birds flying across the upper sky"></div>
    <div class="window-art" role="img" aria-label="Narrow panel with a pale standing figure beneath a branching crack of light"></div>
    <h1 class="title">
      <span class="title__main">DIARY</span>
      <span class="title__sub">Toward</span>
      <span class="title__accent">Stillness</span>
    </h1>
    <p class="subtitle">A 13-WEEK QMR EXPLORATION</p>
  </main>
</body>
</html>
```